Workers comp/Business Ins/ Payroll- Postcard

I own an insurance agency.  I'm interested in getting some professional advice on how to design a message for what i want to sell.  The products I want to sell are 1) Workers compensation 2) business Insurance 3) Payroll processing. They are integrated together but I'm not sure if it's too much to put on a postcard and if I don't put it on a postcard I could be missing out on sales.
I have the ability to look up what Insurance company a business has their workers compensation  policy with, along with their expiration date.  Based on that information I can tell if the business is overpaying for their Workers compensation. insurance. Most companies are overpaying so I can usually save a company money very quickly if I can get in front of them. Some businesses work with a broker such as myself and buy a policy. When it's done this way, the business ESTIMATES his payroll for the year and at the end of the year they have to complete an audit to find out the actual payroll. Based on audit, they will either owe more money if they were low or get money back if they were high. The other way a business buys a workers comp. policy is with their payroll company. The payroll company will place the policy on Pay -as- you -go which means when you pay your employees every week they  will also calculate how much the workers comp premium is for the week and take that amount out of their checking account. This method avoids large down payments, helps with cash flow and should be very accurate at the end of the policy term.  This is by far the best way to do this for the businessowner. My company also has payroll company and we do this for the insured as well. However, most payroll company's such as QRT and Wagelon charge the customer $15 every time they do this so if it's weekly it is another $780 a year.  We also complete the insured's audit for them which is a big headache for the businessowner.
One of our biggest benefits of doing business with our company is we have a  Steady Rate Forever. When you sign up your base price will never increase. Payroll companies are famous for "discounting a new client" only to increase the rate in a few months later. Our service is also superior to the other payroll companies who use overseas service centers. We have staff within our office and we can answer questions quickly. We usually save businesses money on  their Payroll processing but it's not what we focus on- We focus on the Service.
Business Insurance- One of our main companies that we represent is Brindle Insurance. Brindle is very competitive and we usually write business accounts where we save the business owner money but offer superior coverages.
in summary, I'm offering 1) better workers compensation rates 2) Pay as you go workers comp. 3) Steady Rate, audits done for you, and superior customer service with our payroll company 4) savings on their business insurance with superior coverages.
Sometimes when we talk to an insured we may start with just their payroll and later get the WC and business liability. Each account is different and we do not pressure people to make decisions and we do what is right for them.  The biggest takeaway is we take some things off the plate for the businessowner where they can make just one phone call to get what they need done.  Our Website is www.harbor-mutual.example. my email is tomk@harbor-mutual.example if you have any questions.
Thank You
Tom Kessor

Target Market(s)
Small business owners 1-50 employees
Industry/Entity Type
Insurance and Payroll
Font styles to use
Other font styles liked:
- Let designer choose

Colors
Designer to choose colors to be used in the design.
Requirements
Must have
- It shouldn't be boring- needs to stand out- can use 6x11 inch postcard

Nice to have
- I like humor but not a must

Should not have
- Nothing I can think of

```html
<!DOCTYPE html>
<html lang="en">
<head>
<meta charset="utf-8">
<title>Harbor Mutual Insurance – Postcard</title>
<link href="https://fonts.googleapis.com/css2?family=Montserrat:wght@600;800&family=Nunito+Sans:wght@400;700;800&display=swap" rel="stylesheet">
<style>
:root{
  --page:#e9e9ea;
  --card:#ffffff;
  --red-dark:#6e1214;
  --red:#8c1d1f;
  --red-light:#a3302f;
  --ink:#2b2b2b;
  --grey:#6d6e71;
  --grey-light:#f0f0f0;
  --stamp:#8e8f92;
}
*{box-sizing:border-box;margin:0;padding:0}
html,body{width:750px;height:1200px;overflow:hidden;background:var(--page)}
body{font-family:"Nunito Sans",Arial,sans-serif;color:var(--ink);position:relative}
.card{position:absolute;left:25px;width:700px;height:381px;background:var(--card);overflow:hidden;box-shadow:0 3px 10px rgba(0,0,0,.18)}
.card--front{top:199px}
.card--back{top:620px}
.card svg.art{position:absolute;left:0;top:0;width:700px;height:381px}

.headline{position:absolute;left:38px;top:33px;list-style:none;font-family:"Montserrat",Arial,sans-serif;font-weight:800;color:#fff;font-size:23px;line-height:26px;letter-spacing:.2px}
.headline li{position:relative;padding-left:12px}
.headline li::before{content:"";position:absolute;left:0;top:11px;width:4px;height:4px;border-radius:50%;background:#c2585a}

.brand{position:absolute;text-align:center;font-family:"Montserrat",Arial,sans-serif;font-weight:600;color:var(--grey)}
.brand__name{display:block;letter-spacing:1px}
.brand__sub{display:block;letter-spacing:8px}
.card--front .brand{left:408px;top:62px;width:292px}
.card--front .brand__name{font-size:25px;line-height:28px}
.card--front .brand__sub{font-size:10px;margin-top:2px}
.card--back .brand{left:400px;top:46px;width:190px}
.card--back .brand__name{font-size:16px;line-height:18px}
.card--back .brand__sub{font-size:6.5px;letter-spacing:5px;margin-top:1px}

.copy{position:absolute;font-size:8.7px;line-height:11.2px;color:var(--ink)}
.copy p+p{margin-top:11px}
.copy b{font-weight:800}
.card--front .copy{left:38px;top:145px;width:318px}

.card--back .intro{left:38px;top:20px;width:320px}
.summary{position:absolute;left:38px;top:126px;width:340px;color:#fff;font-size:8.7px;line-height:11.2px}
.summary h2{font-size:8.9px;font-weight:800}
.summary ol{list-style:none;counter-reset:n}
.summary li{counter-increment:n;position:relative;padding-left:13px}
.summary li::before{content:counter(n);position:absolute;left:0;top:2px;width:8px;height:8px;border-radius:50%;background:#b94a4c;font-size:5.5px;line-height:8px;text-align:center;font-weight:800}
.photos{position:absolute;left:38px;top:203px;display:flex;gap:2px}
.photos div{width:109px;height:71px;border-radius:6px;border:1.5px solid #fff}
.photo-laptop{background:linear-gradient(135deg,#eef1f5,#b9c3cf)}
.photo-meeting{background:linear-gradient(135deg,#c9ccd0,#5d5f63)}
.photo-finance{background:linear-gradient(135deg,#6b7078,#2a2d33)}
.card--back .takeaway{left:38px;top:288px;width:300px}
.contact{position:absolute;left:0;top:327px;width:380px;height:54px;background:var(--grey-light)}
.contact__item{position:absolute;top:10px;font-size:8.2px;line-height:11px;white-space:nowrap}
.contact__item strong{display:flex;align-items:center;gap:3px;color:var(--red);font-weight:800;font-size:9px;line-height:14px;white-space:nowrap}
.contact__item strong i{display:inline-block;flex:none;width:8px;height:8px;border-radius:50%;background:var(--red)}
.contact__item small{display:block;font-style:italic;font-size:5px;padding-left:15px}
.contact__web{left:38px}
.contact__mail{left:205px}
.contact__rule{position:absolute;left:198px;top:12px;width:1px;height:22px;background:var(--red)}
.stamp{position:absolute;left:607px;top:21px;width:67px;height:67px;background:var(--stamp)}
</style>
</head>
<body>

<section class="card card--front">
  <svg class="art" viewBox="0 0 700 381">
    <defs>
      <linearGradient id="bandRed" x1="0" y1="0" x2="1" y2="1">
        <stop offset="0" stop-color="#6e1214"/>
        <stop offset=".6" stop-color="#8c1d1f"/>
        <stop offset="1" stop-color="#a3302f"/>
      </linearGradient>
      <linearGradient id="deskTone" x1="0" y1="0" x2="1" y2="1">
        <stop offset="0" stop-color="#1d1f24"/>
        <stop offset=".45" stop-color="#b07a45"/>
        <stop offset=".7" stop-color="#d9d4cb"/>
        <stop offset="1" stop-color="#2a2c31"/>
      </linearGradient>
    </defs>
    <path d="M0,12 L409,12 L366,129 L0,129 Z" fill="url(#bandRed)"/>
    <path role="img" aria-label="Photo: business people signing a contract at a wooden desk" d="M366,129 L700,129 L700,381 L415,381 C380,330 358,230 366,129 Z" fill="url(#deskTone)"/>
  </svg>
  <ul class="headline">
    <li>WORKERS COMPENSATION</li>
    <li>BUSINESS INSURANCE</li>
    <li>PAYROLL PROCESSING.</li>
  </ul>
  <div class="brand"><span class="brand__name">HARBOR MUTUAL</span><span class="brand__sub">INSURANCE</span></div>
  <div class="copy">
    <p>I have the ability to look up what Insurance company a business has their <b>workers compensation policy</b> with, along with their expiration date. Based on that information I can tell if the business is overpaying for their <b>Workers compensation. insurance.</b> Most companies are overpaying so I can usually <b>save a company money very quickly</b> if I can get in front of them.</p>
    <p>The other way a business buys a workers comp. policy is with their <b>payroll company.</b> The payroll company will place the policy on Pay -as- you -go which means when you pay your employees every week they will also calculate how much the workers comp premium is for the week and take that amount out of their checking account. This method <b>avoids large down payments, helps with cash flow</b> and should be <b>very accurate</b> at the end of the policy term. This is by far the best way to do this for the businessowner. most payroll company's such as <b>QRT and Wagelon</b> charge the customer <b>$15</b> every time they do this so if it's weekly it is another <b>$780 a year.</b></p>
    <p>We also complete the insured's audit for them which is a big headache for the businessowner.</p>
  </div>
</section>

<section class="card card--back">
  <svg class="art" viewBox="0 0 700 381">
    <path d="M0,116 L398,116 L398,240 L0,240 Z" fill="var(--red-dark)"/>
    <path d="M352,0 C430,110 430,270 349,381" fill="none" stroke="var(--red-dark)" stroke-width="7"/>
    <path d="M368,0 C446,110 446,270 365,381" fill="none" stroke="var(--red)" stroke-width="1.5"/>
  </svg>
  <div class="copy intro">
    <p>One of our biggest benefits of doing business with our company is we have a <b>Steady Rate Forever.</b> When you sign up your base <b>price will never increase.</b> Payroll companies are famous for <b>"discounting a new client"</b> only to increase the rate in a few months later. Our service is also superior to the other payroll companies who use overseas service centers. We have staff within our office and we can answer questions quickly. We usually save businesses money on their Payroll processing but it's not what we focus on- We focus on the Service.</p>
  </div>
  <div class="summary">
    <h2>in summary, I'm offering</h2>
    <ol>
      <li>better workers compensation rates</li>
      <li>Pay as you go workers comp.</li>
      <li>Steady Rate, audits done for you, and superior customer service</li>
      <li>with our payroll company</li>
      <li>savings on their business insurance with superior coverages.</li>
    </ol>
  </div>
  <div class="photos">
    <div class="photo-laptop" role="img" aria-label="Photo: hands reviewing paperwork beside a laptop"></div>
    <div class="photo-meeting" role="img" aria-label="Photo: team meeting around a table"></div>
    <div class="photo-finance" role="img" aria-label="Photo: payments and finance icons over a desk"></div>
  </div>
  <div class="copy takeaway">
    <p>The biggest takeaway is we take some things off the plate for the businessowner where they can make just one phone call to get what they need done.</p>
  </div>
  <div class="contact">
    <div class="contact__item contact__web">Our Website is<strong><i></i>www.harbor-mutual.example</strong></div>
    <div class="contact__rule"></div>
    <div class="contact__item contact__mail">my email is<strong><i></i>tomk@harbor-mutual.example</strong><small>if you have any questions</small></div>
  </div>
  <div class="brand"><span class="brand__name">HARBOR MUTUAL</span><span class="brand__sub">INSURANCE</span></div>
  <div class="stamp"></div>
</section>

</body>
</html>
```